Non fiction book cover. The book advises how to get a new job.

The book size will be 20cm high by 13cm wide and I need a front cover which can wrap around to the back. This book has a serious message, but I've tried to make it quite light to read and accessible. So I don't want a cover that is too dour or serious and not frivolous either. At the end of the project, I will need a high resolution 3D image of the book, included as part of the package.<br/>The Title of the book is:- "Past Fifty? Hunting for your new role?<br/>by Colin Marsh-Whitby".<br/>I am thinking of a light yellow background, with a striking image to attract attention. The image and words should be clear and sharp.<br/>Here is the, BACK COVER wording.<br/>"This book tells you clearly and simply the steps that you need to take, to get a job, once you’re over 50.<br/>It advises you on the techniques to use to write a killer CV.<br/>It explains how to ensure that your CV attention.<br/>It shows the best way to approach your local job agency.<br/>It demonstrates the best way to use your network.<br/><br/>This book, written by someone with 30 years’ experience in the recruitment industry, gives you ALL the answers.<br/>Whether you are a top executive or someone after some local part time work, then this book is for you. <br/>With the help of this book you will secure your next position.<br/>

Target Market(s)

UK, over 50s, male and female.

Font styles to use
Serif

Colors
fbee3e

Requirements
Must have
• A clear uncluttered cover.
Should not have
• Fussy and over complicated

```html
<!DOCTYPE html>
<html lang="en">
<head>
<meta charset="utf-8">
<title>Past Fifty? Hunting for your new role? — Colin Marsh-Whitby</title>
<link rel="stylesheet" href="https://fonts.googleapis.com/css2?family=Anton&family=Oswald:wght@400;500;700&display=swap">
<style>
  :root {
    --backdrop: #e7e7e7;
    --cover-yellow: #e8dc3c;
    --ink: #0b0b0b;
    --accent-red: #d9202a;
  }
  * { margin: 0; padding: 0; box-sizing: border-box; }
  html, body {
    width: 1200px;
    height: 800px;
    overflow: hidden;
    background: var(--backdrop);
  }
  .canvas {
    position: relative;
    width: 1200px;
    height: 800px;
  }
  .cover {
    position: absolute;
    left: 350px;
    top: 17px;
    width: 500px;
    height: 766px;
    background: var(--cover-yellow);
    color: var(--ink);
  }
  .title {
    position: absolute;
    left: 0;
    width: 500px;
    text-align: center;
    font-family: "Anton", "Impact", sans-serif;
    font-weight: 400;
    line-height: 1;
    text-transform: uppercase;
    white-space: nowrap;
  }
  .title-line-1 { top: 62px; font-size: 118px; letter-spacing: 2px; }
  .title-line-2 { top: 156px; font-size: 140px; letter-spacing: -1px; }

  .subtitle {
    position: absolute;
    right: 212px;
    top: 338px;
    text-align: right;
    font-family: "Oswald", "Arial Narrow", sans-serif;
    font-weight: 700;
    font-size: 40px;
    line-height: 46px;
    text-transform: uppercase;
    white-space: nowrap;
  }
  .subtitle-ring {
    position: absolute;
    left: 297px;
    top: 313px;
    width: 146px;
    height: 146px;
    border: 6px solid var(--ink);
    border-radius: 50%;
    display: flex;
    flex-direction: column;
    align-items: center;
    justify-content: center;
    font-family: "Oswald", "Arial Narrow", sans-serif;
    font-weight: 700;
    text-transform: uppercase;
    line-height: 1;
    white-space: nowrap;
  }
  .subtitle-ring .ring-lead { font-size: 30px; }
  .subtitle-ring .ring-key {
    font-size: 42px;
    color: var(--accent-red);
    margin-top: 4px;
  }
  .climber-figure {
    position: absolute;
    left: 292px;
    top: 462px;
    width: 110px;
    height: 228px;
    background: linear-gradient(180deg, rgba(26,26,20,0.55), rgba(26,26,20,0.25));
    border-radius: 4px;
  }
  .author {
    position: absolute;
    left: 0;
    width: 500px;
    top: 700px;
    text-align: center;
    font-family: "Oswald", "Arial Narrow", sans-serif;
    font-weight: 500;
    font-size: 38px;
    line-height: 1;
    letter-spacing: 4px;
    text-transform: uppercase;
    white-space: nowrap;
  }
</style>
</head>
<body>
  <main class="canvas">
    <section class="cover">
      <h1 class="title title-line-1">Past</h1>
      <div class="title title-line-2">Fifty?</div>
      <p class="subtitle">Hunting<br>for your</p>
      <div class="subtitle-ring">
        <span class="ring-lead">New</span>
        <span class="ring-key">Role?</span>
      </div>
      <div class="climber-figure" role="img" aria-label="Silhouette of a person climbing a rope that hangs from the circle"></div>
      <p class="author">Colin Marsh-Whitby</p>
    </section>
  </main>
</body>
</html>
```